Stationery Design Project

I would like to get the designs done for the following:
1. Envelop - Big (for A4 documents) and Small for Folded document.
2. Letterpad
3. Stationary Pad (for Internal Use)
Thanks,
Tushar
- We are open to different ideas and design concept, it should be unique and should still maintain a corporate look.
Velqo-Fulllogo - This is the complete logo set.
Velqo Logo Only - this is only the complete logo of the company
Velqo Arrow - Arrow is a minimum form of the logo, which represents "velqo"
Velqomin-Tag - Velqo Minimum name with the tag-line can be used also as a logo
Note: We have attached Velqo - Letter Pad Format - Sample.pdf file for just showing you an example for the letterpad.

```html
<!DOCTYPE html>
<html lang="en">
<head>
<meta charset="utf-8">
<title>Velqo Stationery Set</title>
<link href="https://fonts.googleapis.com/css2?family=Open+Sans:wght@400;600;700&display=swap" rel="stylesheet">
<style>
:root{
  --bg:#bdbdbd;
  --paper:#ffffff;
  --ink:#3a3a3a;
  --muted:#8a8a8a;
  --rule:#9a9a9a;
  --green:#4a9a3a;
  --sky:#6f8fc8;
  --red:#d8363a;
  --navy:#2f3f8e;
  --accent:#c8102e;
  --flap:#f1f1f1;
}
*{margin:0;padding:0;box-sizing:border-box}
html,body{width:1200px;height:810px;overflow:hidden}
body{background:var(--bg);font-family:"Open Sans",Arial,sans-serif;color:var(--ink);position:relative}
.sheet{position:absolute;background:var(--paper);overflow:hidden}
.brand{position:absolute;display:flex;align-items:center;gap:6px;font-weight:400;color:var(--ink);line-height:1}
.brand-square{display:inline-block;background:var(--ink)}
.stripe-block{position:absolute;background:linear-gradient(180deg,var(--green) 0%,var(--sky) 35%,var(--red) 65%,var(--navy) 100%)}
.band{position:absolute;right:0;width:max-content;color:#fff;font-weight:400;display:flex;align-items:center;justify-content:flex-end;white-space:nowrap;clip-path:polygon(var(--slant) 0,100% 0,100% 100%,0 100%)}
.band.green{background:var(--green)}.band.sky{background:var(--sky)}.band.red{background:var(--red)}.band.navy{background:var(--navy)}
.flap{position:absolute;left:0;top:0;width:100%;background:linear-gradient(180deg,var(--flap),#fafafa);border-bottom:1px solid #e4e4e4}

/* small envelope */
.envelope-small{left:112px;top:129px;width:299px;height:174px}
.envelope-small .flap{height:30px}
.envelope-small .brand{right:18px;top:55px;font-size:17px}
.envelope-small .band{--slant:7px;height:9px;font-size:4.6px;padding:0 5px 0 12px}

/* business cards */
.card{top:130px;width:151px;height:91px}
.card-front{left:433px}
.card-front .brand{left:34px;top:34px;font-size:19px}
.card-back{left:603px;width:152px}
.card-person{position:absolute;left:4px;top:27px;width:72px;text-align:center}
.card-person .name{color:var(--accent);font-weight:700;font-size:8.5px}
.card-person .role{font-weight:700;font-size:5.5px;margin-top:1px}
.card-person .phone{color:var(--accent);font-size:5.5px;margin-top:12px}
.card-person .mail{font-size:5.5px}
.card-divider{position:absolute;left:74px;top:10px;width:1px;height:72px;background:var(--accent)}
.card-company{position:absolute;left:77px;top:32px;width:74px;text-align:center;font-size:3.8px;line-height:1.5}
.card-company .co{color:var(--accent);font-weight:600;font-size:5.5px;margin-bottom:1px}

/* letterhead */
.letterhead{left:114px;top:330px;width:290px;height:409px}
.letterhead .brand{left:18px;top:24px;font-size:22px}
.lh-contacts{position:absolute;right:12px;top:15px;font-size:7.5px;line-height:12px}
.lh-contacts li{list-style:none;display:flex;align-items:center;gap:4px}
.lh-contacts svg{width:8px;height:8px}
.lh-rule{position:absolute;left:140px;right:10px;top:55px;height:1px;background:var(--rule)}
.lh-wash{position:absolute;left:0;right:0;background:linear-gradient(180deg,#f6f6f6,#fdfdfd)}
.lh-wash.one{top:58px;height:80px}
.lh-wash.two{top:141px;height:142px}
.lh-motif{position:absolute;left:176px;top:188px;width:106px;height:126px;background:radial-gradient(circle,#eeeeee 0%,rgba(238,238,238,0) 70%)}
.letterhead .stripe-block.side{right:0;top:95px;width:18px;height:81px}
.letterhead .stripe-block.foot{left:0;top:290px;width:16px;height:81px}
.lh-footer{position:absolute;left:0;right:0;top:371px;text-align:center;font-size:8px;line-height:11px}
.lh-footer .co{color:var(--accent);font-weight:600;font-size:9px;display:inline-block;border-bottom:1px solid var(--rule);padding:0 2px;margin-bottom:2px}

/* large envelope */
.envelope-large{left:441px;top:242px;width:300px;height:498px}
.envelope-large .flap{height:55px}
.envelope-large .brand{left:16px;top:420px;font-size:26px}
.envelope-large .band{--slant:14px;height:19px;font-size:8.4px;padding:0 6px 0 22px}

/* writing pad */
.pad{left:792px;top:254px;width:326px;height:459px}
.pad .brand{left:96px;top:194px;font-size:26px}
.pad .stripe-block.side{right:0;top:34px;width:20px;height:90px}
.pad .stripe-block.foot{left:0;top:326px;width:18px;height:91px}
</style>
</head>
<body>

<section class="sheet envelope-small" aria-label="Small envelope">
  <div class="flap"></div>
  <div class="brand"><span class="brand-square" style="width:11px;height:11px"></span>velqo</div>
  <div class="band green" style="bottom:27px;min-width:70px">SY. 18, Nirmal Park, Plot No. 12</div>
  <div class="band sky" style="bottom:18px;min-width:84px">Sagar Vihar Society, Adajan - 395009</div>
  <div class="band red" style="bottom:9px;min-width:98px">Surat Gujarat, India, Ph. +91-261-4102000</div>
  <div class="band navy" style="bottom:0;min-width:112px">Mail- info@velqo.co.in, Web- www.velqo.co.in</div>
</section>

<section class="sheet card card-front" aria-label="Business card front">
  <div class="brand"><span class="brand-square" style="width:12px;height:12px"></span>velqo</div>
</section>

<section class="sheet card card-back" aria-label="Business card back">
  <div class="card-person">
    <div class="name">Kiran Mehta</div>
    <div class="role">Director</div>
    <div class="phone">Ph. 91-98XXXXXX10</div>
    <div class="mail">Mail- info@velqo.co.in</div>
  </div>
  <div class="card-divider"></div>
  <div class="card-company">
    <div class="co">Velqo Industries Limited</div>
    <div>SY. 18, Nirmal Park, Plot No. 12,</div>
    <div>Sagar Vihar Society, Adajan - 395009</div>
    <div>Surat Gujarat, India, Ph. +91-261-4102000</div>
  </div>
</section>

<section class="sheet letterhead" aria-label="Letterhead">
  <div class="lh-wash one"></div>
  <div class="lh-wash two"></div>
  <div class="lh-motif" role="img" aria-label="Faint brand decoration area"></div>
  <div class="brand"><span class="brand-square" style="width:14px;height:14px"></span>velqo</div>
  <ul class="lh-contacts">
    <li><svg viewBox="0 0 10 10"><path d="M2 1l2 2-1 1.2c.6 1.3 1.5 2.2 2.8 2.8L7 6l2 2-1.2 1.4C4.5 9 1 5.5.6 2.2z" fill="#2f3f8e"/></svg>+91-261-4102000</li>
    <li><svg viewBox="0 0 10 10"><rect x="0.5" y="2" width="9" height="6" fill="#d8363a"/><path d="M.5 2L5 5.5 9.5 2" stroke="#fff" fill="none"/></svg>info@velqo.co.in</li>
    <li><svg viewBox="0 0 10 10"><path d="M5 1L.5 5H2v4h6V5h1.5z" fill="#b5651d"/></svg>www.velqo.co.in</li>
  </ul>
  <div class="lh-rule"></div>
  <div class="stripe-block side" role="img" aria-label="Colour band decoration"></div>
  <div class="stripe-block foot" role="img" aria-label="Colour band decoration"></div>
  <div class="lh-footer">
    <div class="co">Velqo Industries Limited</div>
    <div>SY. 18, Nirmal Park, Plot No. 12, Sagar Vihar Society, Adajan - 395009, Surat</div>
    <div>Gujarat, India, Ph. +91-261-4102000</div>
  </div>
</section>

<section class="sheet envelope-large" aria-label="Large envelope">
  <div class="flap"></div>
  <div class="brand"><span class="brand-square" style="width:18px;height:18px"></span>velqo</div>
  <div class="band green" style="bottom:57px;min-width:140px">SY. 18, Nirmal Park, Plot No. 12</div>
  <div class="band sky" style="bottom:38px;min-width:165px">Sagar Vihar Society, Adajan - 395009</div>
  <div class="band red" style="bottom:19px;min-width:190px">Surat Gujarat, India, Ph. +91-261-4102000</div>
  <div class="band navy" style="bottom:0;min-width:215px">Mail-info@velqo.co.in, Web- www.velqo.co.in</div>
</section>

<section class="sheet pad" aria-label="Writing pad">
  <div class="stripe-block side" role="img" aria-label="Colour band decoration"></div>
  <div class="brand"><span class="brand-square" style="width:18px;height:18px"></span>velqo</div>
  <div class="stripe-block foot" role="img" aria-label="Colour band decoration"></div>
</section>

</body>
</html>
```